Dog Coat Drive for San Francisco Homeless Pets

- one page, full color, flyer to advertise a winter dog coat drive.- requesting use of an image of pit bull type or chihuahua type dog in a coat - 2 size versions - 8.5 inch by 11 inch to be printed and a square design to be posted on FB, Instagram and websites

Font styles to use
Serif
Sans Serif

Colors

Designer to choose colors to be used in the design.

```html
<!DOCTYPE html>
<html lang="en">
<head>
<meta charset="utf-8">
<title>Dog Coat Drive</title>
<link rel="stylesheet" href="https://fonts.googleapis.com/css2?family=Baloo+2:wght@500;600;700;800&display=swap">
<style>
  :root {
    --blue: #17a9e4;
    --blue-dark: #0e8fcf;
    --blue-light: #5cc8f2;
    --ink: #454545;
    --ink-soft: #5a5a5a;
    --rule: #c9c9c9;
    --paper: #ffffff;
    --blanket: #cdbcae;
    --fur: #b59a83;
  }
  * { margin: 0; padding: 0; box-sizing: border-box; }
  html, body { width: 1200px; height: 1200px; overflow: hidden; background: var(--paper); }
  body { font-family: "Baloo 2", sans-serif; color: var(--ink); }
  .flyer { position: relative; width: 1200px; height: 1200px; overflow: hidden; background: var(--paper); }

  .hero-photo {
    position: absolute; left: 0; top: 0; width: 1200px; height: 860px;
    background:
      radial-gradient(ellipse 230px 260px at 790px 330px, var(--fur) 0%, rgba(181,154,131,0) 100%),
      radial-gradient(ellipse 420px 420px at 780px 450px, var(--blanket) 0%, rgba(205,188,174,0.6) 55%, rgba(205,188,174,0) 100%),
      linear-gradient(90deg, #ffffff 0%, #f7f6f6 30%, #e7e3e1 60%, #ddd8d4 100%);
  }
  .hero-fade {
    position: absolute; left: 0; top: 0; width: 1200px; height: 860px;
    background:
      linear-gradient(90deg, rgba(255,255,255,0.95) 0%, rgba(255,255,255,0.75) 35%, rgba(255,255,255,0) 60%),
      linear-gradient(180deg, rgba(255,255,255,0) 70%, #ffffff 100%);
  }

  .brand { position: absolute; left: 52px; top: 74px; display: flex; align-items: center; gap: 14px; }
  .brand-mark { width: 70px; height: 70px; border-radius: 50%; background: var(--blue); }
  .brand-name { font-size: 60px; font-weight: 700; color: var(--blue); line-height: 1; }
  .brand-tagline { position: absolute; left: 220px; top: 146px; font-size: 25px; font-weight: 700; color: #222; }

  .headline { position: absolute; left: 44px; top: 262px; font-size: 74px; font-weight: 800; color: var(--blue); line-height: 1; white-space: nowrap; }
  .subhead { position: absolute; left: 50px; top: 336px; font-size: 42px; font-weight: 700; color: var(--ink-soft); line-height: 1; white-space: nowrap; }

  .dates {
    position: absolute; left: 46px; top: 426px; width: 484px; height: 54px;
    border-radius: 27px; background: var(--blue);
    color: #fff; font-size: 26px; font-weight: 700; line-height: 56px; text-align: center;
  }

  .appeal { position: absolute; left: 48px; top: 514px; font-size: 29px; font-weight: 700; line-height: 45.5px; color: var(--ink); white-space: nowrap; }

  .bubble { position: absolute; left: 830px; top: 440px; width: 370px; height: 380px; }
  .bubble-text {
    position: absolute; left: 853px; top: 524px; width: 310px;
    font-size: 60px; font-weight: 800; color: #fff; line-height: 64px; text-align: center; white-space: nowrap;
  }
  .bubble-text span { display: block; }

  .partners-title {
    position: absolute; left: 48px; top: 842px; width: 1104px;
    display: flex; align-items: center; gap: 22px;
    font-size: 25px; font-weight: 700; color: var(--blue); white-space: nowrap;
  }
  .partners-title::before, .partners-title::after { content: ""; flex: 1; height: 2px; background: var(--blue); }

  .partner { position: absolute; }
  .partner-badge { position: absolute; }
  .partner-name { font-size: 20px; font-weight: 700; color: var(--blue); line-height: 26px; white-space: nowrap; }
  .partner-line { display: flex; align-items: center; gap: 8px; font-size: 17px; font-weight: 700; color: var(--ink); line-height: 28px; white-space: nowrap; }
  .partner-line svg { width: 14px; height: 14px; fill: var(--blue); flex: none; }
  .divider { position: absolute; width: 1px; background: var(--rule); }
</style>
</head>
<body>
<main class="flyer">
  <div class="hero-photo" role="img" aria-label="Photo of a small pug wrapped in a soft beige knit blanket on a white bed"></div>
  <div class="hero-fade"></div>

  <div class="brand">
    <span class="brand-mark"></span>
    <span class="brand-name">WarmPawsBus</span>
  </div>
  <div class="brand-tagline">Mobile Pet Care Team</div>

  <h1 class="headline">Dog Coat Drive</h1>
  <h2 class="subhead">for SF Navigation Centers</h2>

  <div class="dates">From December through February</div>

  <p class="appeal">Please donate new &amp; gently used<br>dog coats, sweaters and jackets<br>for Navigation Center dogs<br>whose owners are working to<br>prevent and end their<br>homelessness</p>

  <svg class="bubble" viewBox="0 0 370 380" aria-hidden="true">
    <path d="M262 318 L318 372 L226 346 Z" fill="var(--blue)"/>
    <circle cx="178" cy="184" r="176" fill="var(--blue-light)" opacity="0.55"/>
    <circle cx="178" cy="184" r="164" fill="var(--blue)"/>
  </svg>
  <div class="bubble-text"><span>Baby,</span><span>It’s Cold</span><span>Outside!</span></div>

  <h3 class="partners-title">Coat drop partners and locations</h3>

  <svg class="partner-badge" style="left:44px;top:912px;width:120px;height:90px" viewBox="0 0 120 90" aria-hidden="true">
    <circle cx="70" cy="42" r="40" fill="#1b5aa6"/>
  </svg>
  <div class="partner" style="left:186px;top:914px">
    <div class="partner-name">Bay Animal Shelter</div>
    <div class="partner-line"><svg viewBox="0 0 24 24"><path d="M12 2C8 2 5 5 5 9c0 5 7 13 7 13s7-8 7-13c0-4-3-7-7-7zm0 9.5a2.5 2.5 0 110-5 2.5 2.5 0 010 5z"/></svg>410 Harbor Street</div>
    <div class="partner-line"><svg viewBox="0 0 24 24"><path d="M6.6 10.8a15 15 0 006.6 6.6l2.2-2.2c.3-.3.7-.4 1-.2 1.1.4 2.3.6 3.6.6.6 0 1 .4 1 1V20c0 .6-.4 1-1 1A17 17 0 013 4c0-.6.4-1 1-1h3.5c.6 0 1 .4 1 1 0 1.2.2 2.4.6 3.6.1.3 0 .7-.2 1z"/></svg>415-555-0142</div>
  </div>

  <div class="divider" style="left:378px;top:906px;height:110px"></div>

  <svg class="partner-badge" style="left:396px;top:932px;width:220px;height:60px" viewBox="0 0 220 60" aria-hidden="true">
    <rect x="4" y="8" width="212" height="44" rx="4" fill="#c8832c"/>
  </svg>
  <div class="partner" style="left:636px;top:914px">
    <div class="partner-name">The Critter Corner</div>
    <div class="partner-line"><svg viewBox="0 0 24 24"><path d="M12 2C8 2 5 5 5 9c0 5 7 13 7 13s7-8 7-13c0-4-3-7-7-7zm0 9.5a2.5 2.5 0 110-5 2.5 2.5 0 010 5z"/></svg>82 Maple Street</div>
    <div class="partner-line"><svg viewBox="0 0 24 24"><path d="M6.6 10.8a15 15 0 006.6 6.6l2.2-2.2c.3-.3.7-.4 1-.2 1.1.4 2.3.6 3.6.6.6 0 1 .4 1 1V20c0 .6-.4 1-1 1A17 17 0 013 4c0-.6.4-1 1-1h3.5c.6 0 1 .4 1 1 0 1.2.2 2.4.6 3.6.1.3 0 .7-.2 1z"/></svg>415-555-0187</div>
  </div>

  <div class="divider" style="left:840px;top:906px;height:110px"></div>

  <svg class="partner-badge" style="left:864px;top:910px;width:100px;height:100px" viewBox="0 0 100 100" aria-hidden="true">
    <circle cx="50" cy="50" r="47" fill="#111"/>
    <circle cx="50" cy="50" r="47" fill="none" stroke="#e36a1e" stroke-width="4"/>
  </svg>
  <div class="partner" style="left:978px;top:914px">
    <div class="partner-name">Hillside Pet Co.</div>
    <div class="partner-line"><svg viewBox="0 0 24 24"><path d="M12 2C8 2 5 5 5 9c0 5 7 13 7 13s7-8 7-13c0-4-3-7-7-7zm0 9.5a2.5 2.5 0 110-5 2.5 2.5 0 010 5z"/></svg>905 Cedar Street</div>
    <div class="partner-line"><svg viewBox="0 0 24 24"><path d="M6.6 10.8a15 15 0 006.6 6.6l2.2-2.2c.3-.3.7-.4 1-.2 1.1.4 2.3.6 3.6.6.6 0 1 .4 1 1V20c0 .6-.4 1-1 1A17 17 0 013 4c0-.6.4-1 1-1h3.5c.6 0 1 .4 1 1 0 1.2.2 2.4.6 3.6.1.3 0 .7-.2 1z"/></svg>415-555-0163</div>
  </div>

  <svg class="partner-badge" style="left:100px;top:1042px;width:104px;height:110px" viewBox="0 0 104 110" aria-hidden="true">
    <circle cx="52" cy="55" r="48" fill="#8cc563"/>
  </svg>
  <div class="partner" style="left:240px;top:1058px">
    <div class="partner-name">Happy Tails Pet Services</div>
    <div class="partner-line"><svg viewBox="0 0 24 24"><path d="M12 2C8 2 5 5 5 9c0 5 7 13 7 13s7-8 7-13c0-4-3-7-7-7zm0 9.5a2.5 2.5 0 110-5 2.5 2.5 0 010 5z"/></svg>36 Ocean Drive, Pacifica</div>
    <div class="partner-line"><svg viewBox="0 0 24 24"><path d="M6.6 10.8a15 15 0 006.6 6.6l2.2-2.2c.3-.3.7-.4 1-.2 1.1.4 2.3.6 3.6.6.6 0 1 .4 1 1V20c0 .6-.4 1-1 1A17 17 0 013 4c0-.6.4-1 1-1h3.5c.6 0 1 .4 1 1 0 1.2.2 2.4.6 3.6.1.3 0 .7-.2 1z"/></svg>650-555-0119</div>
  </div>

  <div class="divider" style="left:528px;top:1050px;height:110px"></div>

  <svg class="partner-badge" style="left:564px;top:1082px;width:244px;height:40px" viewBox="0 0 244 40" aria-hidden="true">
    <rect x="0" y="2" width="244" height="36" fill="#1d3a5c"/>
  </svg>
  <div class="partner" style="left:823px;top:1058px">
    <div class="partner-name">The Fido Center</div>
    <div class="partner-line"><svg viewBox="0 0 24 24"><path d="M12 2C8 2 5 5 5 9c0 5 7 13 7 13s7-8 7-13c0-4-3-7-7-7zm0 9.5a2.5 2.5 0 110-5 2.5 2.5 0 010 5z"/></svg>720 Seaview Avenue, Pacifica</div>
    <div class="partner-line"><svg viewBox="0 0 24 24"><path d="M6.6 10.8a15 15 0 006.6 6.6l2.2-2.2c.3-.3.7-.4 1-.2 1.1.4 2.3.6 3.6.6.6 0 1 .4 1 1V20c0 .6-.4 1-1 1A17 17 0 013 4c0-.6.4-1 1-1h3.5c.6 0 1 .4 1 1 0 1.2.2 2.4.6 3.6.1.3 0 .7-.2 1z"/></svg>650-555-0175</div>
  </div>
</main>
</body>
</html>
```